Brochure Projecct

I need a brochure created for my company, which will be sent to customers via email in PDF format. I have uploaded the company logo with this project, which I want incorporated in the design.

Designers should view the company website at www.brightcounselpages.com. I want the brochure to compliment the website (i.e., very clean design). I would also like pictures added to the brochure to make the design visually stunning.

In terms of content, I need four pages in the brochure to add four separate sections of content (one section per page). The four sections of content will be as follows (1) Search Engine Optimization Benefits (2) Increased Client Retention (3) Showcase Your Law Firm (4) Maximize Your Online ROI (5) Pricing Plans. I will give the content to the winning designer to add to the project. Each individual content section will have four subsection titles after which content of approximately 100 to 200 words will appear.

Designers can decide if other pages should be added to the brochure (i.e., a "cover page" that would have little content, but be visually appealing like the cover of a book - - - a "back page" that may just have the logo, contact information, etc).

My company address and email address should be prominently featured through every page (address: 2715 West Juniper Avenue, Suite 1400, Scottsdale, Arizona 85317; email: sales@brightcounselpages.com).

Industry/Entity Type

It Company

Requirements
Must have
• Clean look but visually stunning incorporating the design of the website at brightcounselpages.com as well as the logo. Also, room for content as set forth in the description of this project.

```html
<!DOCTYPE html>
<html lang="en">
<head>
<meta charset="utf-8">
<title>Bright Counsel Pages – Brochure Spreads</title>
<link rel="stylesheet" href="https://fonts.googleapis.com/css2?family=PT+Sans:ital,wght@0,400;0,700;1,400;1,700&display=swap">
<style>
:root{
  --stage:#1b1b1b;
  --paper:#ffffff;
  --teal:#1ba6b5;
  --teal-light:#63cdd8;
  --teal-dark:#0d7f90;
  --title:#3d3d3d;
  --body:#5a5a5a;
  --rule:#cfd3d5;
  --footer:#2a9bb0;
}
*{box-sizing:border-box;margin:0;padding:0}
html,body{width:1200px;height:1200px;overflow:hidden;background:var(--stage);font-family:"PT Sans",Arial,sans-serif}
.canvas{position:relative;width:1200px;height:1200px}

.page{position:absolute;width:363px;height:467px;background:var(--paper);overflow:hidden}
.band-top{position:absolute;left:0;top:0;width:100%;height:5px;background:linear-gradient(var(--teal-light),var(--teal-dark))}
.notch-top{position:absolute;left:50%;top:5px;width:12px;height:6px;margin-left:-6px}
.band-bottom{position:absolute;left:0;bottom:0;width:100%;height:10px;background:linear-gradient(var(--teal-light),var(--teal-dark))}
.notch-bottom{position:absolute;left:50%;bottom:10px;width:12px;height:6px;margin-left:-6px}
.footer-rule{position:absolute;left:34px;right:34px;top:441px;height:1px;background:var(--rule)}
.footer-address{position:absolute;left:0;right:0;top:445px;text-align:center;font-style:italic;font-size:5.4px;color:var(--footer);z-index:3}
.page-number{position:absolute;left:0;right:0;top:424px;text-align:center;font-style:italic;font-size:7px;color:var(--body);z-index:3}

.page-title{position:absolute;left:34px;top:24px;font-style:italic;font-size:20px;line-height:21px;color:var(--title)}
.page-title .line-one{display:block;padding-left:10px}
.title-rule{position:absolute;left:34px;top:70px;width:296px;height:8px}

.brand{position:absolute;right:30px;top:24px;width:52px;text-align:center;font-size:7.2px;line-height:8px;color:var(--title)}
.brand-dot{display:block;width:20px;height:20px;margin:0 auto 3px;border-radius:50%;background:var(--teal)}

.column{position:absolute;top:84px;width:146px}
.column.left{left:34px}
.column.right{left:184px}
.sub-heading{font-style:italic;font-size:10px;line-height:12px;color:var(--title);margin:6px 0 4px}
.column p{font-size:4.4px;line-height:5.8px;color:var(--body);margin-bottom:5px}

.photo{position:absolute}

/* cover */
.cover-photo{left:0;top:5px;width:363px;height:436px;
  background:radial-gradient(ellipse 45% 50% at 20% 70%,#e7c2a8 0%,rgba(231,194,168,0) 100%),
             radial-gradient(ellipse 18% 30% at 62% 55%,#f1cbb3 0%,rgba(241,203,179,0) 100%),
             linear-gradient(180deg,#ffffff 0%,#f6f3f1 60%,#ebe3de 100%)}
.bubble{position:absolute;width:81px;height:51px;border-radius:50%;
  background:radial-gradient(ellipse at 40% 30%,#8fe0e8 0%,#28aebd 55%,#127f8f 100%);
  box-shadow:0 2px 4px rgba(0,0,0,.25);
  display:flex;align-items:center;justify-content:center;text-align:center;
  font-style:italic;font-weight:700;font-size:7.6px;line-height:8.4px;color:#fff;z-index:2}
.cover-brand{position:absolute;left:196px;top:76px;width:110px;text-align:center;font-size:15px;line-height:16px;color:var(--title);z-index:2}
.cover-brand .brand-dot{width:34px;height:34px;margin-bottom:4px}
.tagline{position:absolute;left:56px;top:372px;width:240px;font-style:italic;font-size:17.5px;line-height:19px;color:var(--title);z-index:2}
.tagline .line-one{display:block;padding-left:30px}
.tagline-rule{position:absolute;left:56px;top:412px;width:296px;height:1px;background:var(--rule);z-index:2}
</style>
</head>
<body>
<div class="canvas">

<!-- Cover -->
<section class="page" style="left:30px;top:34px">
  <div class="photo cover-photo" role="img" aria-label="Smiling woman reaching toward the viewer with her finger touching a floating button"></div>
  <div class="band-top"></div>
  <div class="cover-brand"><span class="brand-dot"></span>Bright Counsel Pages</div>
  <div class="bubble" style="left:60px;top:29px">Search Engine<br>Optimization<br>Benefits</div>
  <div class="bubble" style="left:65px;top:122px">Increased<br>Client Retention</div>
  <div class="bubble" style="left:147px;top:191px">Showcase<br>Your Law Firm</div>
  <div class="bubble" style="left:267px;top:187px">Maximize<br>Your Online ROI</div>
  <div class="tagline"><span class="line-one">A local list</span>of experienced Arazona Lawyers</div>
  <div class="tagline-rule"></div>
  <div class="footer-address">2715 West Juniper Avenue, Suite 1400, Scottsdale, Arizona 85317; email: sales@brightcounselpages.com</div>
  <div class="band-bottom"></div>
  <svg class="notch-bottom" viewBox="0 0 12 6"><polygon points="0,6 6,0 12,6" fill="#63cdd8"/></svg>
</section>

<!-- Search Engine Optimization Benefits -->
<section class="page" style="left:418px;top:34px">
  <div class="band-top"></div>
  <svg class="notch-top" viewBox="0 0 12 6"><polygon points="0,0 12,0 6,6" fill="#1295a6"/></svg>
  <h1 class="page-title"><span class="line-one">Search Engine</span>Optimization Benefits</h1>
  <svg class="title-rule" viewBox="0 0 296 8"><polyline points="0,1 24,1 29,6 34,1 296,1" fill="none" stroke="#cfd3d5" stroke-width="1"/></svg>
  <div class="brand"><span class="brand-dot"></span>Bright Counsel Pages</div>
  <div class="column left">
    <h2 class="sub-heading">First sub heading</h2>
    <p>Clients searching for legal help start online, and a clear listing places your practice in front of them at the right moment. We write focused pages, tune every profile and track each visit so you can see exactly which work brings new cases. Our team reviews your results every month and adjusts keywords, photos and reviews, keeping your firm visible while competitors fall behind in local searches.</p>
    <p>Clients searching for legal help start online, and a clear listing places your practice in front of them at the right moment. We write focused pages, tune every profile and track each visit so you can see exactly which work brings new cases.</p>
    <h2 class="sub-heading">Second sub heading</h2>
    <p>Clients searching for legal help start online, and a clear listing places your practice in front of them at the right moment. We write focused pages, tune every profile and track each visit so you can see exactly which work brings new cases. Our team reviews your results every month and adjusts keywords, photos and reviews, keeping your firm visible while competitors fall behind in local searches. Clients searching for legal help start online, and a clear listing places your practice in front of them at the right moment. We write focused pages, tune every profile and track each visit so you can see exactly which work brings new cases.</p>
    <h2 class="sub-heading">Third sub heading</h2>
    <p>Clients searching for legal help start online, and a clear listing places your practice in front of them at the right moment. We write focused pages, tune every profile and track each visit so you can see exactly which work brings new cases. Our team reviews your results every month and adjusts keywords, photos and reviews, keeping your firm visible while competitors fall behind in local searches.</p>
    <p>Our team reviews your results every month and adjusts keywords, photos and reviews, keeping your firm visible while competitors fall behind in local searches.</p>
  </div>
  <div class="column right" style="top:88px">
    <p>Clients searching for legal help start online, and a clear listing places your practice in front of them at the right moment. We write focused pages, tune every profile and track each visit so you can see exactly which work brings new cases. Our team reviews your results every month and adjusts keywords, photos and reviews, keeping your firm visible while competitors fall behind in local searches.</p>
    <h2 class="sub-heading">Fourth sub heading</h2>
    <p>Clients searching for legal help start online, and a clear listing places your practice in front of them at the right moment. We write focused pages, tune every profile and track each visit so you can see exactly which work brings new cases. Our team reviews your results every month and adjusts keywords, photos and reviews, keeping your firm visible while competitors fall behind in local searches.</p>
    <p>Clients searching for legal help start online, and a clear listing places your practice in front of them at the right moment. We write focused pages, tune every profile and track each visit so you can see exactly which work brings new cases. Our team reviews your results every month and adjusts keywords, photos and reviews, keeping your firm visible while competitors fall behind in local searches.</p>
  </div>
  <div class="photo" style="left:197px;top:261px;width:126px;height:172px;background:linear-gradient(180deg,#6fd6df 0%,#36b6c4 30%,#e9ddd6 70%,#ffffff 100%)" role="img" aria-label="Finger pressing a glowing teal SEO key"></div>
  <div class="page-number">1</div>
  <div class="footer-rule"></div>
  <div class="footer-address">2715 West Juniper Avenue, Suite 1400, Scottsdale, Arizona 85317; email: sales@brightcounselpages.com</div>
  <div class="band-bottom"></div>
  <svg class="notch-bottom" viewBox="0 0 12 6"><polygon points="0,6 6,0 12,6" fill="#63cdd8"/></svg>
</section>

<!-- Increased Client Retention -->
<section class="page" style="left:807px;top:34px">
  <div class="band-top"></div>
  <svg class="notch-top" viewBox="0 0 12 6"><polygon points="0,0 12,0 6,6" fill="#1295a6"/></svg>
  <h1 class="page-title"><span class="line-one">Increased</span>Client Retention</h1>
  <svg class="title-rule" viewBox="0 0 296 8"><polyline points="0,1 24,1 29,6 34,1 296,1" fill="none" stroke="#cfd3d5" stroke-width="1"/></svg>
  <div class="brand"><span class="brand-dot"></span>Bright Counsel Pages</div>
  <div class="column left">
    <h2 class="sub-heading">First sub heading</h2>
    <p>Clients searching for legal help start online, and a clear listing places your practice in front of them at the right moment. We write focused pages, tune every profile and track each visit so you can see exactly which work brings new cases. Our team reviews your results every month and adjusts keywords, photos and reviews, keeping your firm visible while competitors fall behind in local searches.</p>
    <p>Clients searching for legal help start online, and a clear listing places your practice in front of them at the right moment. We write focused pages, tune every profile and track each visit so you can see exactly which work brings new cases.</p>
    <h2 class="sub-heading">Second sub heading</h2>
    <p>Clients searching for legal help start online, and a clear listing places your practice in front of them at the right moment. We write focused pages, tune every profile and track each visit so you can see exactly which work brings new cases. Our team reviews your results every month and adjusts keywords, photos and reviews, keeping your firm visible while competitors fall behind in local searches. Clients searching for legal help start online, and a clear listing places your practice in front of them at the right moment. We write focused pages, tune every profile and track each visit so you can see exactly which work brings new cases.</p>
  </div>
  <div class="column right">
    <h2 class="sub-heading">Third sub heading</h2>
    <p>Clients searching for legal help start online, and a clear listing places your practice in front of them at the right moment. We write focused pages, tune every profile and track each visit so you can see exactly which work brings new cases. Our team reviews your results every month and adjusts keywords, photos and reviews, keeping your firm visible while competitors fall behind in local searches.</p>
    <p>Clients searching for legal help start online, and a clear listing places your practice in front of them at the right moment. We write focused pages, tune every profile and track each visit so you can see exactly which work brings new cases. Our team reviews your results every month and adjusts keywords, photos and reviews, keeping your firm visible while competitors fall behind in local searches.</p>
    <h2 class="sub-heading">Fourth sub heading</h2>
    <p>Clients searching for legal help start online, and a clear listing places your practice in front of them at the right moment. We write focused pages, tune every profile and track each visit so you can see exactly which work brings new cases. Our team reviews your results every month and adjusts keywords, photos and reviews, keeping your firm visible while competitors fall behind in local searches.</p>
    <p>Clients searching for legal help start online, and a clear listing places your practice in front of them at the right moment. We write focused pages, tune every profile and track each visit so you can see exactly which work brings new cases. Our team reviews your results every month and adjusts keywords, photos and reviews, keeping your firm visible while competitors fall behind in local searches.</p>
  </div>
  <div class="photo" style="left:34px;top:321px;width:295px;height:116px;background:linear-gradient(90deg,#3b3d40 0%,#d9a48e 40%,#e8b7a0 60%,#5a5c60 100%)" role="img" aria-label="Two business people in suits shaking hands"></div>
  <div class="page-number">2</div>
  <div class="footer-rule"></div>
  <div class="footer-address">2715 West Juniper Avenue, Suite 1400, Scottsdale, Arizona 85317; email: sales@brightcounselpages.com</div>
  <div class="band-bottom"></div>
  <svg class="notch-bottom" viewBox="0 0 12 6"><polygon points="0,6 6,0 12,6" fill="#63cdd8"/></svg>
</section>

<!-- Showcase Your Law Firm -->
<section class="page" style="left:30px;top:551px">
  <div class="band-top"></div>
  <svg class="notch-top" viewBox="0 0 12 6"><polygon points="0,0 12,0 6,6" fill="#1295a6"/></svg>
  <h1 class="page-title"><span class="line-one">Showcase</span>Your Law Firm</h1>
  <svg class="title-rule" viewBox="0 0 296 8"><polyline points="0,1 24,1 29,6 34,1 296,1" fill="none" stroke="#cfd3d5" stroke-width="1"/></svg>
  <div class="brand"><span class="brand-dot"></span>Bright Counsel Pages</div>
  <div class="column left">
    <h2 class="sub-heading">First sub heading</h2>
    <p>Clients searching for legal help start online, and a clear listing places your practice in front of them at the right moment. We write focused pages, tune every profile and track each visit so you can see exactly which work brings new cases. Our team reviews your results every month and adjusts keywords, photos and reviews, keeping your firm visible while competitors fall behind in local searches.</p>
    <p>Clients searching for legal help start online, and a clear listing places your practice in front of them at the right moment. We write focused pages, tune every profile and track each visit so you can see exactly which work brings new cases.</p>
    <h2 class="sub-heading">Second sub heading</h2>
    <p>Clients searching for legal help start online, and a clear listing places your practice in front of them at the right moment. We write focused pages, tune every profile and track each visit so you can see exactly which work brings new cases.</p>
  </div>
  <div class="column right" style="top:94px">
    <p>Clients searching for legal help start online, and a clear listing places your practice in front of them at the right moment. We write focused pages, tune every profile and track each visit so you can see exactly which work brings new cases. Our team reviews your results every month and adjusts keywords, photos and reviews, keeping your firm visible while competitors fall behind in local searches.</p>
    <h2 class="sub-heading">Third sub heading</h2>
    <p>Clients searching for legal help start online, and a clear listing places your practice in front of them at the right moment. We write focused pages, tune every profile and track each visit so you can see exactly which work brings new cases. Our team reviews your results every month and adjusts keywords, photos and reviews, keeping your firm visible while competitors fall behind in local searches.</p>
    <p>Clients searching for legal help start online, and a clear listing places your practice in front of them at the right moment. We write focused pages, tune every profile and track each visit so you can see exactly which work brings new cases. Our team reviews your results every month and adjusts keywords, photos and reviews, keeping your firm visible while competitors fall behind in local searches.</p>
    <h2 class="sub-heading">Fourth sub heading</h2>
    <p>Clients searching for legal help start online, and a clear listing places your practice in front of them at the right moment. We write focused pages, tune every profile and track each visit so you can see exactly which work brings new cases. Our team reviews your results every month and adjusts keywords, photos and reviews, keeping your firm visible while competitors fall behind in local searches.</p>
    <p>Clients searching for legal help start online, and a clear listing places your practice in front of them at the right moment. We write focused pages, tune every profile and track each visit so you can see exactly which work brings new cases. Our team reviews your results every month and adjusts keywords, photos and reviews, keeping your firm visible while competitors fall behind in local searches.</p>
  </div>
  <div class="photo" style="left:0;top:242px;width:184px;height:193px;background:linear-gradient(135deg,#cfc7bf 0%,#e9e4df 45%,#bfc4c8 75%,#ffffff 100%)" role="img" aria-label="Confident businesswoman with arms crossed in front of colleagues meeting in an office"></div>
  <div class="page-number">3</div>
  <div class="footer-rule"></div>
  <div class="footer-address">2715 West Juniper Avenue, Suite 1400, Scottsdale, Arizona 85317; email: sales@brightcounselpages.com</div>
  <div class="band-bottom"></div>
  <svg class="notch-bottom" viewBox="0 0 12 6"><polygon points="0,6 6,0 12,6" fill="#63cdd8"/></svg>
</section>

<!-- Maximize Your Online ROI -->
<section class="page" style="left:418px;top:551px">
  <div class="band-top"></div>
  <svg class="notch-top" viewBox="0 0 12 6"><polygon points="0,0 12,0 6,6" fill="#1295a6"/></svg>
  <h1 class="page-title"><span class="line-one">Maximize</span>Your Online ROI</h1>
  <svg class="title-rule" viewBox="0 0 296 8"><polyline points="0,1 24,1 29,6 34,1 296,1" fill="none" stroke="#cfd3d5" stroke-width="1"/></svg>
  <div class="brand"><span class="brand-dot"></span>Bright Counsel Pages</div>
  <div class="column left">
    <h2 class="sub-heading">First sub heading</h2>
    <p>Clients searching for legal help start online, and a clear listing places your practice in front of them at the right moment. We write focused pages, tune every profile and track each visit so you can see exactly which work brings new cases. Our team reviews your results every month and adjusts keywords, photos and reviews, keeping your firm visible while competitors fall behind in local searches.</p>
    <p>Clients searching for legal help start online, and a clear listing places your practice in front of them at the right moment. We write focused pages, tune every profile and track each visit so you can see exactly which work brings new cases.</p>
    <h2 class="sub-heading">Second sub heading</h2>
    <p>Clients searching for legal help start online, and a clear listing places your practice in front of them at the right moment. We write focused pages, tune every profile and track each visit so you can see exactly which work brings new cases. Our team reviews your results every month and adjusts keywords, photos and reviews, keeping your firm visible while competitors fall behind in local searches.</p>
    <h2 class="sub-heading">Third sub heading</h2>
    <p>Clients searching for legal help start online, and a clear listing places your practice in front of them at the right moment. We write focused pages, tune every profile and track each visit so you can see exactly which work brings new cases. Our team reviews your results every month and adjusts keywords, photos and reviews, keeping your firm visible while competitors fall behind in local searches.</p>
  </div>
  <div class="column right" style="top:94px">
    <p>Clients searching for legal help start online, and a clear listing places your practice in front of them at the right moment. We write focused pages, tune every profile and track each visit so you can see exactly which work brings new cases.</p>
    <h2 class="sub-heading">Fourth sub heading</h2>
    <p>Clients searching for legal help start online, and a clear listing places your practice in front of them at the right moment. We write focused pages, tune every profile and track each visit so you can see exactly which work brings new cases. Our team reviews your results every month and adjusts keywords, photos and reviews, keeping your firm visible while competitors fall behind in local searches.</p>
  </div>
  <div class="photo" style="left:190px;top:196px;width:173px;height:239px;background:linear-gradient(160deg,#ffffff 0%,#efe6dc 35%,#d8c8b6 65%,#9aa3ab 100%)" role="img" aria-label="Businesswoman in a light suit smiling while working on a laptop"></div>
  <div class="page-number">5</div>
  <div class="footer-rule"></div>
  <div class="footer-address">2715 West Juniper Avenue, Suite 1400, Scottsdale, Arizona 85317; email: sales@brightcounselpages.com</div>
  <div class="band-bottom"></div>
  <svg class="notch-bottom" viewBox="0 0 12 6"><polygon points="0,6 6,0 12,6" fill="#63cdd8"/></svg>
</section>

<!-- Pricing Plans -->
<section class="page" style="left:807px;top:551px">
  <div class="band-top"></div>
  <svg class="notch-top" viewBox="0 0 12 6"><polygon points="0,0 12,0 6,6" fill="#1295a6"/></svg>
  <h1 class="page-title"><span class="line-one">Pricing</span>Plans</h1>
  <svg class="title-rule" viewBox="0 0 296 8"><polyline points="0,1 24,1 29,6 34,1 296,1" fill="none" stroke="#cfd3d5" stroke-width="1"/></svg>
  <div class="brand"><span class="brand-dot"></span>Bright Counsel Pages</div>
  <div class="page-number">6</div>
  <div class="footer-rule"></div>
  <div class="footer-address">2715 West Juniper Avenue, Suite 1400, Scottsdale, Arizona 85317; email: sales@brightcounselpages.com</div>
  <div class="band-bottom"></div>
  <svg class="notch-bottom" viewBox="0 0 12 6"><polygon points="0,6 6,0 12,6" fill="#63cdd8"/></svg>
</section>

</div>
</body>
</html>
```